IT Company based on Biology Business Needs a Professional Web Design

We need a professional business website design for a new company called 'Vast KELP'. We develop the machine learning solutions especially focused on deep learning algorithms for biology industry. Our initial product is a vision detection on biological images to help doctors diagnose the symptoms. We would like to see designs that use the color green.

Industry/Entity Type

Business

Number of Pages Required

5+ page

```html
<!DOCTYPE html>
<html lang="en">
<head>
<meta charset="utf-8">
<title>Vast KELP – Biological Research</title>
<link href="https://fonts.googleapis.com/css2?family=Open+Sans:wght@300;400;600;700&display=swap" rel="stylesheet">
<style>
:root{
  --green:#6cbf3f;
  --green-dark:#2f8a2a;
  --hero-a:#5fb83a;
  --hero-b:#2e8d2c;
  --ink:#222;
  --text:#666;
  --muted:#888;
  --soft-bg:#f6f6f6;
  --card:#ececec;
  --footer:#3b3b3b;
  --footer-text:#cfcfcf;
}
*{margin:0;padding:0;box-sizing:border-box}
html,body{width:1200px;height:2975px;overflow:hidden}
body{font-family:"Open Sans",Arial,sans-serif;color:var(--ink);background:#fff;position:relative}
.abs{position:absolute}
section,header,footer{position:absolute;left:0;width:1200px}
.center{text-align:center;left:0;width:1200px}

/* header */
.site-header{top:0;height:134px;background:#fff}
.brand{left:100px;top:44px;font-size:30px;font-weight:600;color:var(--green);letter-spacing:.5px;display:flex;align-items:center;gap:10px}
.brand-dot{width:18px;height:18px;border-radius:50%;background:var(--green)}
.nav{top:58px;left:326px;display:flex;gap:0}
.nav a{font-size:13px;color:#222;text-decoration:none;padding:5px 10px;margin-right:14px;line-height:14px}
.nav a.active{background:var(--green);color:#fff}
.call{left:834px;top:56px;width:218px;height:32px;border:1px solid var(--green);font-size:12px;font-weight:600;line-height:30px;padding-left:10px;color:#222}
.call span{font-weight:400;color:#444}
.call-icon{position:absolute;right:-1px;top:-1px;width:32px;height:32px;background:var(--green);display:flex;align-items:center;justify-content:center}
.search{left:1066px;top:56px;width:31px;height:31px;border:1px solid #333;display:flex;align-items:center;justify-content:center}

/* hero */
.hero{top:134px;height:446px;background:linear-gradient(120deg,var(--hero-a),#7cc658 45%,var(--hero-b))}
.hero-title{top:100px;font-size:56px;font-weight:400;color:#fff;line-height:68px}
.hero-title span{font-size:50px;display:block}
.hero-sub{top:236px;font-size:21px;color:#eaf7e2;font-weight:300}
.hero-btn{left:470px;top:296px;width:260px;height:54px;border:1px solid #fff;display:flex}
.hero-btn .label{flex:1;color:#fff;font-size:15px;font-weight:600;line-height:52px;text-align:center}
.hero-btn .go{width:52px;background:var(--green-dark);display:flex;align-items:center;justify-content:center}

/* shared section heads */
.sec-title{font-size:31px;color:var(--green);font-weight:400}
.sec-sub{font-size:14.5px;color:#222}

/* about */
.about{top:580px;height:492px;background:var(--soft-bg)}
.about .sec-title{top:70px}
.about .sec-sub{top:118px}
.about-text{left:230px;top:190px;width:740px;font-size:13.5px;line-height:30px;color:var(--text);text-align:center}
.btn-grey{left:533px;top:370px;width:134px;height:42px;background:#dcdcdc;color:#444;font-size:14px;text-align:center;line-height:42px}

/* process */
.process{top:1072px;height:426px;background:#fff}
.process .sec-title{top:70px}
.process .sec-sub{top:118px}
.step{width:300px;text-align:center;top:188px}
.step-ring{width:78px;height:78px;border:1.5px solid var(--green);border-radius:50%;margin:0 auto;display:flex;align-items:center;justify-content:center}
.step h3{font-size:14px;font-weight:700;margin-top:28px;color:#111}
.step p{font-size:13px;color:var(--text);line-height:23px;margin-top:6px}
.step-line{height:1px;background:#ddd;top:227px}

/* testimonials */
.testimonials{top:1498px;height:512px;background:var(--soft-bg)}
.testimonials .sec-title{top:55px}
.testimonials .sec-sub{top:107px}
.quote{width:455px;height:182px;background:var(--card);box-shadow:2px 3px 5px rgba(0,0,0,.18);top:180px;padding:20px 28px 0 28px;font-size:13.3px;line-height:23px;color:var(--text)}
.quote-mark{position:absolute;right:30px;bottom:8px;font-size:80px;font-weight:700;color:#cfcfcf;line-height:60px;font-style:italic}
.avatar{width:70px;height:70px;border-radius:50%;background:linear-gradient(#c9c9c9,#8a8a8a)}
.person{top:402px}
.person h4{font-size:17px;font-weight:600;color:#111}
.person p{font-size:13.5px;color:#333;margin-top:2px}

/* news */
.news{top:2010px;height:688px;background:#fff}
.news .sec-title{top:70px}
.news .sec-sub{top:118px}
.card{width:287px;height:414px;top:194px;background:#f3f3f3;text-align:center}
.card-photo{height:214px;background:linear-gradient(160deg,#e8eef3,#b9c9d6 60%,#8aa2b8)}
.card h3{font-size:16px;font-weight:600;margin-top:26px;color:#111}
.card .meta{font-size:12px;color:#222;margin-top:6px}
.card p{font-size:12.5px;color:var(--text);line-height:21px;margin:10px 24px 0}
.card .more{font-size:12.5px;font-weight:600;color:#111;margin-top:14px}

/* footer */
.site-footer{top:2698px;height:277px;background:var(--footer);color:var(--footer-text)}
.f-head{font-size:15px;font-weight:600;color:#fff;top:52px}
.f-row{display:flex;align-items:center;gap:14px;font-size:13px}
.f-ico{width:18px;display:flex;justify-content:center}
.social-ring{width:30px;height:30px;border:1.5px solid #aaa;border-radius:50%}
.f-brand{left:720px;width:276px;top:82px;text-align:center;font-size:28px;font-weight:600;color:#aaa}
.f-copy{left:680px;width:356px;top:180px;text-align:center;font-size:12.5px}
.f-links{left:680px;width:356px;top:210px;text-align:center;font-size:12.5px}
</style>
</head>
<body>

<header class="site-header">
  <div class="abs brand"><span class="brand-dot"></span>VAST KELP</div>
  <nav class="abs nav">
    <a class="active">HOME</a><a>ABOUT US</a><a>OUR SERVICES</a><a>RESOURSES</a><a>CONTACT US</a>
  </nav>
  <div class="abs call">CALL US AT : <span>800-555-0143</span>
    <div class="call-icon"><svg width="16" height="16" viewBox="0 0 24 24"><path fill="#fff" d="M6.6 10.8a15 15 0 0 0 6.6 6.6l2.2-2.2c.3-.3.7-.4 1-.2 1.1.4 2.3.6 3.6.6.6 0 1 .4 1 1V20c0 .6-.4 1-1 1A17 17 0 0 1 3 4c0-.6.4-1 1-1h3.5c.6 0 1 .4 1 1 0 1.3.2 2.5.6 3.6.1.3 0 .7-.2 1z"/></svg></div>
  </div>
  <div class="abs search"><svg width="14" height="14" viewBox="0 0 24 24"><circle cx="10" cy="10" r="7" fill="none" stroke="#222" stroke-width="3"/><path d="M15 15l6 6" stroke="#222" stroke-width="3"/></svg></div>
</header>

<section class="hero" role="img" aria-label="Scientist working with a microscope in a laboratory, under a green tint">
  <h1 class="abs center hero-title">EXPERT IN<span>BIOLOGICAL RESEARCH</span></h1>
  <p class="abs center hero-sub">About Employee Engagement And Custoer Satisfaction</p>
  <div class="abs hero-btn"><div class="label">GET STARTED</div>
    <div class="go"><svg width="16" height="14" viewBox="0 0 16 14"><path fill="#fff" d="M0 4h8V0l8 7-8 7v-4H0z"/></svg></div>
  </div>
</section>

<section class="about">
  <h2 class="abs center sec-title">ABOUT US</h2>
  <p class="abs center sec-sub">There are many variations of passages of Lorem Ipsum available</p>
  <p class="abs about-text">"Sed ut perspiciatis unde omnis iste natus error sit voluptatem accusantium doloremque laudantium, totam rem aperiam, eaque ipsa quae ab illo inventore veritatis et quasi architecto beatae vitae dicta sunt explicabo. Nemo enim ipsam voluptatem quia voluptas sit aspernatur aut odit aut fugit, sed quia consequuntur magni dolores eos qui ratione voluptatem sequi nesciunt. Neque porro quisquam est, qui dolorem ipsum quia dolor sit amet, consectetur, adipisci velit, sed quia non numquam eius modi tempora incidunt ut labore et dolore magnam aliquam quaerat voluptatem.</p>
  <div class="abs btn-grey">READ MORE</div>
</section>

<section class="process">
  <h2 class="abs center sec-title">HOW IT WORK</h2>
  <p class="abs center sec-sub">There are many variations of passages of Lorem Ipsum available</p>
  <div class="abs step-line" style="left:325px;width:176px"></div>
  <div class="abs step-line" style="left:690px;width:176px"></div>
  <div class="abs step" style="left:84px"><div class="step-ring"><svg width="34" height="34"><circle cx="17" cy="17" r="12" fill="none" stroke="#6cbf3f" stroke-width="1.5"/><circle cx="17" cy="17" r="4" fill="#6cbf3f"/></svg></div><h3>SED DOLOR AMIT CON</h3><p>Sed ut perspiciatis unde omnis iste natus error<br>sit voluptatem accusantium doloremque</p></div>
  <div class="abs step" style="left:436px"><div class="step-ring"><svg width="34" height="34"><circle cx="17" cy="17" r="12" fill="none" stroke="#6cbf3f" stroke-width="1.5"/><circle cx="17" cy="17" r="4" fill="#6cbf3f"/></svg></div><h3>SED DOLOR AMIT CON</h3><p>Sed ut perspiciatis unde omnis iste natus error<br>sit voluptatem accusantium doloremque</p></div>
  <div class="abs step" style="left:808px"><div class="step-ring"><svg width="34" height="34"><circle cx="17" cy="17" r="12" fill="none" stroke="#6cbf3f" stroke-width="1.5"/><circle cx="17" cy="17" r="4" fill="#6cbf3f"/></svg></div><h3>SED DOLOR AMIT CON</h3><p>Sed ut perspiciatis unde omnis iste natus error<br>sit voluptatem accusantium doloremque</p></div>
</section>

<section class="testimonials">
  <h2 class="abs center sec-title">OUR TESTIMONIALS</h2>
  <p class="abs center sec-sub">There are many variations of passages of Lorem Ipsum available</p>
  <div class="abs quote" style="left:133px">"Sed ut perspiciatis unde omnis iste natus error sit voluptatem accusantium doloremque laudantium, totam rem aperiam, eaque ipsa quae ab illo inventore veritatis et quasi architecto beatae vitae dicta sunt explicabo. Nemo enim ipsam voluptatem quia voluptas sit aspernatur aut odit aut fugit, sed quia consequuntur magni dolores eos qui ratione voluptatem sequi. "<span class="quote-mark">"</span></div>
  <div class="abs quote" style="left:615px">"Sed ut perspiciatis unde omnis iste natus error sit voluptatem accusantium doloremque laudantium, totam rem aperiam, eaque ipsa quae ab illo inventore veritatis et quasi architecto beatae vitae dicta sunt explicabo. Nemo enim ipsam voluptatem quia voluptas sit aspernatur aut odit aut fugit, sed quia consequuntur magni dolores eos qui ratione voluptatem sequi. "<span class="quote-mark">"</span></div>
  <div class="abs avatar" style="left:149px;top:387px" role="img" aria-label="Portrait of client"></div>
  <div class="abs person" style="left:250px"><h4>MARCUS</h4><p>SEO , Owner of Company</p></div>
  <div class="abs avatar" style="left:632px;top:387px" role="img" aria-label="Portrait of client"></div>
  <div class="abs person" style="left:733px"><h4>MARCUS</h4><p>SEO , Owner of Company</p></div>
</section>

<section class="news">
  <h2 class="abs center sec-title">OUR LATEST NEWS</h2>
  <p class="abs center sec-sub">There are many variations of passages of Lorem Ipsum available</p>
  <article class="abs card" style="left:141px"><div class="card-photo" role="img" aria-label="Two researchers in lab coats working at a laboratory bench"></div><h3>SED UT PERSPICIATIS UNDE</h3><div class="meta">24,01,2016 &nbsp;| &nbsp;Comments &nbsp;| &nbsp;Biological</div><p>natus error sit voluptatem accusantium dolor emque laudantium, totam rem ap eriam, eaque ipsa quae ab illo...</p><div class="more">READ MORE</div></article>
  <article class="abs card" style="left:457px"><div class="card-photo" role="img" aria-label="Scientists examining samples at a microscope"></div><h3>SED UT PERSPICIATIS UNDE</h3><div class="meta">24,01,2016 &nbsp;| &nbsp;Comments &nbsp;| &nbsp;Biological</div><p>natus error sit voluptatem accusantium dolor emque laudantium, totam rem ap eriam, eaque ipsa quae ab illo...</p><div class="more">READ MORE</div></article>
  <article class="abs card" style="left:773px"><div class="card-photo" role="img" aria-label="Researchers handling test tubes in a bright laboratory"></div><h3>SED UT PERSPICIATIS UNDE</h3><div class="meta">24,01,2016 &nbsp;| &nbsp;Comments &nbsp;| &nbsp;Biological</div><p>natus error sit voluptatem accusantium dolor emque laudantium, totam rem ap eriam, eaque ipsa quae ab illo...</p><div class="more">READ MORE</div></article>
</section>

<footer class="site-footer">
  <div class="abs f-head" style="left:99px">CONTACT US</div>
  <div class="abs f-row" style="left:99px;top:98px"><span class="f-ico"><svg width="16" height="12" viewBox="0 0 16 12"><rect width="16" height="12" fill="#aaa"/><path d="M0 0l8 6 8-6" fill="none" stroke="#3b3b3b" stroke-width="1.5"/></svg></span>info@vastkelp.com</div>
  <div class="abs f-row" style="left:99px;top:136px;font-weight:600;color:#e6e6e6"><span class="f-ico"><svg width="16" height="16" viewBox="0 0 24 24"><path fill="#bbb" d="M6.6 10.8a15 15 0 0 0 6.6 6.6l2.2-2.2c.3-.3.7-.4 1-.2 1.1.4 2.3.6 3.6.6.6 0 1 .4 1 1V20c0 .6-.4 1-1 1A17 17 0 0 1 3 4c0-.6.4-1 1-1h3.5c.6 0 1 .4 1 1 0 1.3.2 2.5.6 3.6.1.3 0 .7-.2 1z"/></svg></span>800-555-0172 &nbsp;&nbsp; +1-972-555-0190</div>
  <div class="abs f-row" style="left:99px;top:176px;align-items:flex-start"><span class="f-ico"><svg width="14" height="18" viewBox="0 0 14 20"><path fill="#bbb" d="M7 0a7 7 0 0 0-7 7c0 5 7 13 7 13s7-8 7-13a7 7 0 0 0-7-7zm0 10a3 3 0 1 1 0-6 3 3 0 0 1 0 6z"/></svg></span><span style="line-height:20px">418 Harbor Ridge Suite 210,<br>Marlow, TX 75510</span></div>

  <div class="abs f-head" style="left:392px">FOLLOW US</div>
  <div class="abs f-row" style="left:392px;top:88px"><span class="social-ring"></span>Follow us on Chirpline</div>
  <div class="abs f-row" style="left:392px;top:128px"><span class="social-ring"></span>Like Us on Friendbook</div>
  <div class="abs f-row" style="left:392px;top:168px"><span class="social-ring"></span>Join Us on Workring</div>
  <div class="abs f-row" style="left:392px;top:208px"><span class="social-ring"></span>Share Us on Searchly</div>

  <div class="abs f-brand">VAST KELP</div>
  <div class="abs f-copy">© Copyright Vast KELP.com All Right Reserved.</div>
  <div class="abs f-links">Terms &amp; Conditions &nbsp;&nbsp;| &nbsp;&nbsp;Privacy Policy</div>
</footer>

</body>
</html>
```